Home Security Company Business Card

Looking for a eye catching business card that is non traditional and stands out but yet still looks professional. It should include all the pertinent information such as name, title, address, telephone, e-mail, website address should definitely stand out and then finally the logo.

Target Market(s)

Residential and Commercial accounts mostly upscale accounts

Industry/Entity Type

Security

Contact Information for Business Card

Name
Title
Address
Office #
Cell #
E-mail
Website

Font styles to use
Serif
Sans Serif

Requirements
Must have
• Logo, two sided color configuration
Nice to have
• You decide
Should not have
• There really aren't any.

```html
<!DOCTYPE html>
<html lang="en">
<head>
<meta charset="utf-8">
<title>Ironvale Security Systems Inc. — Business Card</title>
<link rel="stylesheet" href="https://fonts.googleapis.com/css2?family=Cinzel:wght@400;500&display=swap">
<style>
  :root {
    --ink: #1c1a1a;
    --brand-red: #7a1410;
    --paper: #ffffff;
  }
  html, body {
    margin: 0;
    padding: 0;
    width: 1200px;
    height: 675px;
    overflow: hidden;
    background: var(--paper);
  }
  .card {
    position: relative;
    width: 1200px;
    height: 675px;
    background: var(--paper);
    font-family: "Cinzel", "Times New Roman", serif;
    color: var(--ink);
  }
  .brand-square {
    position: absolute;
    left: 96px;
    top: 120px;
    width: 150px;
    height: 150px;
    background: var(--brand-red);
  }
  .brand-name {
    position: absolute;
    left: 276px;
    top: 164px;
    margin: 0;
    font-weight: 500;
    color: var(--brand-red);
    line-height: 1;
  }
  .brand-main {
    display: block;
    font-size: 58px;
    letter-spacing: 1px;
  }
  .brand-sub {
    display: block;
    margin-top: 4px;
    font-size: 23px;
    letter-spacing: 0.5px;
  }
  .contact {
    position: absolute;
    right: 22px;
    top: 244px;
    text-align: right;
    font-weight: 400;
  }
  .contact p { margin: 0; }
  .person-name {
    font-size: 66px;
    line-height: 70px;
    letter-spacing: 3px;
  }
  .person-title {
    font-size: 44px;
    line-height: 46px;
    letter-spacing: 2px;
    color: var(--brand-red);
  }
  .contact-line {
    font-size: 42px;
    line-height: 46px;
    letter-spacing: 2px;
  }
  .contact-line.first { margin-top: 4px; }
  .address {
    margin-top: 12px !important;
    font-size: 50px;
    line-height: 55px;
    letter-spacing: 1px;
  }
  .website {
    position: absolute;
    left: 28px;
    bottom: 18px;
    margin: 0;
    font-size: 46px;
    line-height: 1;
    letter-spacing: 1px;
    color: var(--brand-red);
  }
</style>
</head>
<body>
  <main class="card">
    <div class="brand-square"></div>
    <p class="brand-name">
      <span class="brand-main">IRONVALE</span>
      <span class="brand-sub">SECURITY SYSTEMS INC.</span>
    </p>

    <section class="contact">
      <p class="person-name">Jane Doe</p>
      <p class="person-title">President</p>
      <p class="contact-line first">info@ironvale.net</p>
      <p class="contact-line">mobile: 617.555.0142</p>
      <p class="contact-line">toll free: 1.800.555.0199</p>
      <p class="address">48 Ironvale Ave<br>Harlow, MA 02190</p>
    </section>

    <p class="website">WWW.IRONVALE.NET</p>
  </main>
</body>
</html>
```